Business Card Design for new consultancy company

Name of Company: Cobalt Wayline
Nature of Business: Digital Business Consultancy
Specialises in Digital Media Strategy, Digital Business Model Transformation, Over-The-Top (OTT) Development, Web Business Development, Digital Marketing, Web and App Product Development, Design and Innovation

Website: http://www.cobalt-wayline.example

Designs can be of any colour or any number of colours, objective is to give the impression we are a digital trend setter, creative and impactful.

Also please suggest a logo to complement the name and business card.

Target Market(s)

Media Companies, Telcos, Enterprises

Industry/Entity Type

Business

Contact Information for Business Card

Standard business card size. OK with to play with small variations like corners for impact/impression.

Font styles to use
Serif
Sans Serif

Requirements
Must have
• Clarity, Impact, Creativity
Nice to have
• Design should encapsulate professionalism, expertise, yet trend-setting and vibrant for digital consultancy
Should not have
• Messy layout, too gaudy colours or design

```html
<!DOCTYPE html>
<html lang="en">
<head>
<meta charset="utf-8">
<title>Marcus Tan — Cobalt Wayline Business Card</title>
<link rel="stylesheet" href="https://fonts.googleapis.com/css2?family=Cinzel:wght@400;500&family=Josefin+Sans:wght@400&display=swap">
<style>
  :root {
    --page-bg: #ffffff;
    --card-black: #070707;
    --card-grey: #4a4a4a;
    --panel-light: #6a6a6a;
    --panel-dark: #1c1c1c;
    --name-lime: #e2ea2f;
    --text-white: #f2f2f2;
    --rule-grey: #9a9a9a;
  }
  * { box-sizing: border-box; margin: 0; padding: 0; }
  html, body {
    width: 1200px;
    height: 1000px;
    overflow: hidden;
    background: var(--page-bg);
  }
  .canvas {
    position: relative;
    width: 1200px;
    height: 1000px;
  }
  .business-card {
    position: absolute;
    left: 150px;
    top: 243px;
    width: 900px;
    height: 514px;
    overflow: hidden;
    border-radius: 4px;
    background:
      linear-gradient(160deg, var(--card-black) 0%, var(--card-black) 42%, #2a2a2a 62%, var(--card-grey) 78%, #1a1a1a 100%);
    box-shadow: 0 10px 30px rgba(0,0,0,0.25);
  }
  .panel-decoration {
    position: absolute;
    inset: 0;
    width: 900px;
    height: 514px;
  }
  .identity {
    position: absolute;
    left: 150px;
    top: 160px;
    width: 295px;
    text-align: right;
  }
  .identity-name {
    font-family: "Cinzel", serif;
    font-weight: 400;
    font-size: 40px;
    line-height: 1;
    color: var(--name-lime);
    letter-spacing: 0.02em;
  }
  .identity-company {
    margin-top: 4px;
    font-family: "Josefin Sans", sans-serif;
    font-size: 14px;
    letter-spacing: 0.32em;
    text-transform: uppercase;
    color: var(--text-white);
  }
  .divider {
    position: absolute;
    left: 470px;
    top: 130px;
    width: 1px;
    height: 190px;
    background: var(--rule-grey);
  }
  .services {
    position: absolute;
    left: 500px;
    top: 140px;
    list-style: none;
    font-family: "Cinzel", serif;
    font-size: 16px;
    line-height: 25px;
    color: var(--text-white);
  }
  .contact {
    position: absolute;
    left: 170px;
    top: 335px;
    width: 300px;
    font-family: "Cinzel", serif;
    font-size: 15px;
    line-height: 22px;
    color: var(--text-white);
  }
  .contact-phone { padding-left: 90px; }
</style>
</head>
<body>
<main class="canvas">
  <article class="business-card">
    <svg class="panel-decoration" viewBox="0 0 900 514" role="img" aria-label="Angled perforated metal panels decoration">
      <defs>
        <linearGradient id="panelGrad" x1="0" y1="0" x2="1" y2="1">
          <stop offset="0" stop-color="var(--panel-light)"/>
          <stop offset="1" stop-color="var(--panel-dark)"/>
        </linearGradient>
      </defs>
      <polygon points="190,0 390,0 300,150 110,150" fill="url(#panelGrad)" opacity="0.85"/>
      <polygon points="60,150 190,150 150,330 0,330 0,220" fill="url(#panelGrad)" opacity="0.7"/>
      <polygon points="0,360 150,330 120,514 0,514" fill="url(#panelGrad)" opacity="0.6"/>
      <polygon points="200,330 320,330 260,420 160,420" fill="url(#panelGrad)" opacity="0.5"/>
    </svg>

    <header class="identity">
      <h1 class="identity-name">Marcus Tan</h1>
      <p class="identity-company">Cobalt Wayline</p>
    </header>

    <div class="divider"></div>

    <ul class="services">
      <li>Digital Business Consultancy</li>
      <li>Specialises in Digital Media Strategy</li>
      <li>Digital Business Model Transformation</li>
      <li>Over-The-Top (OTT) Development</li>
      <li>Web Business Development</li>
      <li>Digital Marketing</li>
      <li>Web and App Product Development</li>
      <li>Design and Innovation</li>
    </ul>

    <address class="contact">
      <p class="contact-phone">+65 9300-4817</p>
      <p class="contact-email">marcus@cobalt-wayline.example</p>
      <p class="contact-web">www.cobalt-wayline.example</p>
    </address>
  </article>
</main>
</body>
</html>
```